We are looking for a Flyer we will send through the mail for residents of Apartment Buildings

We are a laundry service doing pickup and delivery for the Manhattan Area.
We offer next day delivery on all laundry orders.
we want to send out a flyer to buildings for unbelievable promotion:

50% your first order (coupon code ROVK50)
2nd order FREE! (up to $50)
FREE pickup and delivery
FREE next day service
FREE Kestrel and Plumeo
schedule now on www.brimfold.com!

We offer the cleanest and brightest laundry in the city!
Attached is our logo plus some icons to use

Target Market(s)

females ages 24-40

Industry/Entity Type

Apartment

Font styles to use
Other font styles liked:
• habraba

Requirements
Must have
• modern and clean look
• our logo
• BRIGHT COLORS
• Size of flyer will be 8.52 x 5.47
• Logo font: Harabara
• Slogan font: Swiss 721 Light Extended BT
• Dark blue: C 100 M 88 Y 0 K 0
• Light blue: C 85 M 50 Y 0 K 0
• Orange: C 0 M 80 Y 95 K 0
• Violet: C 85 M 100 Y 0 K 0
Should not have
• we dont want to be too busy

```html
<!DOCTYPE html>
<html lang="en">
<head>
<meta charset="utf-8">
<title>brimfold.com – Laundry Pickup &amp; Delivery Flyer</title>
<link rel="stylesheet" href="https://fonts.googleapis.com/css2?family=Archivo+Black&family=Lexend+Exa:wght@500;700&family=Lexend+Zetta:wght@300&display=swap">
<style>
  :root {
    --frame-teal: #3fdcb4;
    --paper-aqua: #9ffcee;
    --paper-glow: #c4fdf4;
    --edge-dark: #1f4f55;
    --brand-blue: #2f8ff2;
    --deep-blue: #2a6ee0;
    --sky-blue: #3aa0ff;
    --promo-orange: #ff3a1c;
    --promo-shadow: #a51a08;
    --violet: #4b1fc8;
    --badge-yellow: #ffd21a;
    --badge-dark: #151515;
    --badge-green: #3c9a58;
  }
  html, body {
    margin: 0;
    padding: 0;
    width: 1200px;
    height: 900px;
    overflow: hidden;
    background: var(--frame-teal);
  }
  .flyer {
    position: relative;
    width: 1200px;
    height: 900px;
    background: var(--frame-teal);
    overflow: hidden;
    font-family: "Lexend Exa", sans-serif;
  }
  .flyer__paper {
    position: absolute;
    left: 20px;
    top: 10px;
    width: 1162px;
    height: 876px;
    background:
      radial-gradient(ellipse 420px 300px at 0% 0%, var(--paper-glow), transparent 70%),
      radial-gradient(ellipse 420px 260px at 100% 0%, var(--paper-glow), transparent 70%),
      radial-gradient(ellipse 520px 300px at 85% 100%, var(--paper-glow), transparent 70%),
      var(--paper-aqua);
    border-bottom: 3px solid var(--edge-dark);
    border-right: 2px solid var(--edge-dark);
  }
  .hero-basket {
    position: absolute;
    left: 400px;
    top: 16px;
    width: 375px;
    height: 135px;
    border-radius: 50% 50% 45% 45% / 40% 40% 60% 60%;
    background: linear-gradient(180deg, #e8324a 0%, #f05aa8 35%, #3a7ff0 70%, #1d4fb8 100%);
  }
  .brand-name {
    position: absolute;
    left: 0;
    width: 1176px;
    text-align: center;
    top: 146px;
    margin: 0;
    font-weight: 700;
    font-size: 52px;
    letter-spacing: 4px;
    color: var(--sky-blue);
    transform: scaleX(1.25);
    transform-origin: 588px 0;
  }
  .slogan {
    position: absolute;
    left: 0;
    width: 1200px;
    top: 220px;
    margin: 0;
    text-align: center;
    font-family: "Lexend Zetta", sans-serif;
    font-weight: 300;
    font-size: 46px;
    line-height: 48px;
    letter-spacing: 2px;
    color: var(--brand-blue);
  }
  .slogan__accent { color: var(--promo-orange); }
  .promo-big {
    position: absolute;
    margin: 0;
    line-height: 1;
    font-family: "Archivo Black", sans-serif;
    color: var(--promo-orange);
    text-shadow: 2px 3px 0 var(--promo-shadow);
  }
  .promo-big--discount {
    left: 0;
    width: 1236px;
    text-align: center;
    top: 334px;
    font-size: 108px;
    letter-spacing: 4px;
    transform: scaleX(1.38);
    transform-origin: 618px 0;
  }
  .promo-sub {
    position: absolute;
    left: 0;
    width: 1220px;
    text-align: center;
    top: 426px;
    margin: 0;
    font-weight: 700;
    font-size: 34px;
    letter-spacing: 9px;
    color: var(--brand-blue);
  }
  .coupon {
    position: absolute;
    left: 0;
    width: 1220px;
    text-align: center;
    top: 468px;
    margin: 0;
    font-weight: 700;
    font-size: 17px;
    letter-spacing: 4px;
    color: var(--violet);
  }
  .coupon__code { color: var(--promo-orange); }
  .second-order {
    position: absolute;
    right: 68px;
    top: 494px;
    margin: 0;
    text-align: right;
    font-weight: 700;
    font-size: 32px;
    letter-spacing: 4px;
    color: var(--brand-blue);
    line-height: 1;
  }
  .second-order__free {
    font-family: "Archivo Black", sans-serif;
    font-size: 50px;
    letter-spacing: 5px;
    color: var(--promo-orange);
    text-shadow: 1px 2px 0 var(--promo-shadow);
  }
  .second-order__cap {
    display: block;
    margin-top: 6px;
    font-size: 28px;
    letter-spacing: 6px;
  }
  .second-order__cap em { font-style: normal; color: var(--promo-orange); }
  .promo-big--free {
    left: 70px;
    top: 566px;
    font-size: 100px;
    letter-spacing: 6px;
    transform: scaleX(1.38);
    transform-origin: 0 0;
  }
  .perks {
    position: absolute;
    left: 76px;
    top: 658px;
    margin: 0;
    padding: 0;
    list-style: none;
    font-weight: 700;
    font-size: 21px;
    letter-spacing: 5px;
    color: var(--deep-blue);
  }
  .perks__item {
    display: flex;
    align-items: center;
    height: 25px;
  }
  .perks__tick {
    width: 18px;
    height: 14px;
    margin-right: 14px;
  }
  .cta {
    position: absolute;
    left: 74px;
    top: 744px;
    margin: 0;
    font-weight: 700;
    font-size: 20px;
    letter-spacing: 6px;
    color: var(--promo-orange);
  }
  .cta-site {
    position: absolute;
    left: 70px;
    top: 764px;
    margin: 0;
    font-weight: 700;
    font-size: 40px;
    letter-spacing: 8px;
    color: var(--deep-blue);
  }
  .partner-badges {
    position: absolute;
    left: 48px;
    top: 814px;
    width: 460px;
    height: 70px;
  }
</style>
</head>
<body>
<main class="flyer">
  <div class="flyer__paper" role="img" aria-label="Soft background of pale floating soap bubbles"></div>

  <div class="hero-basket" role="img" aria-label="Illustration of a blue laundry basket filled with colourful clothes"></div>

  <h1 class="brand-name">brimfold.com</h1>

  <p class="slogan">We offer the <span class="slogan__accent">cleanest</span> and<br><span class="slogan__accent">brightest</span> laundry in the city!</p>

  <p class="promo-big promo-big--discount">50% OFF</p>
  <p class="promo-sub">on your first order</p>
  <p class="coupon">code <span class="coupon__code">ROVK50</span></p>

  <p class="second-order">2ND ORDER <span class="second-order__free">FREE</span>
    <span class="second-order__cap">(up to <em>$50</em>)</span></p>

  <p class="promo-big promo-big--free">FREE!</p>

  <ul class="perks">
    <li class="perks__item"><svg class="perks__tick" viewBox="0 0 18 14" aria-hidden="true"><path d="M2 8 L7 12 L16 2" fill="none" stroke="var(--violet)" stroke-width="3" stroke-linecap="round" stroke-linejoin="round"/></svg>Pick-up and Delivery</li>
    <li class="perks__item"><svg class="perks__tick" viewBox="0 0 18 14" aria-hidden="true"><path d="M2 8 L7 12 L16 2" fill="none" stroke="var(--violet)" stroke-width="3" stroke-linecap="round" stroke-linejoin="round"/></svg>Next-day Service</li>
    <li class="perks__item"><svg class="perks__tick" viewBox="0 0 18 14" aria-hidden="true"><path d="M2 8 L7 12 L16 2" fill="none" stroke="var(--violet)" stroke-width="3" stroke-linecap="round" stroke-linejoin="round"/></svg>Kestrel and Plumeo</li>
  </ul>

  <p class="cta">Schedule now on</p>
  <p class="cta-site">brimfold.com</p>

  <svg class="partner-badges" viewBox="0 0 460 70" role="img" aria-label="Partner and certification badges">
    <ellipse cx="78" cy="34" rx="56" ry="26" fill="var(--badge-yellow)"/>
    <rect x="156" y="10" width="136" height="48" rx="6" fill="var(--badge-dark)"/>
    <circle cx="385" cy="32" r="33" fill="var(--badge-green)"/>
  </svg>
</main>
</body>
</html>
```